Business Card Design Project

Business Card
We are rebranding with a new logo
Industry/Entity Type
Business
Contact Information for Business Card
Dennis Marlow +61 427581962 dennis@qovo.com.au P.O. Box 872 Kelvindale QLD 4309
Requirements
Must have
- Logo

```html
<!DOCTYPE html>
<html lang="en">
<head>
<meta charset="utf-8">
<title>Qovo International – Business Card</title>
<link rel="stylesheet" href="https://fonts.googleapis.com/css2?family=Arimo:wght@400;700&display=swap">
<style>
  :root {
    --ink: #0e5875;
    --accent: #f26a2e;
    --paper: #ffffff;
    --wash: #e6ecf3;
    --wash-warm: #fdeee2;
  }
  html, body {
    margin: 0;
    padding: 0;
    width: 1200px;
    height: 686px;
    overflow: hidden;
    background: var(--paper);
  }
  .card {
    position: relative;
    width: 1200px;
    height: 686px;
    overflow: hidden;
    font-family: "Arimo", Arial, sans-serif;
    color: var(--ink);
    background: var(--paper);
  }
  .card__backdrop {
    position: absolute;
    inset: 0;
    background:
      radial-gradient(ellipse 260px 420px at 0% 38%, var(--wash-warm) 0%, rgba(253,238,226,0) 70%),
      linear-gradient(160deg, var(--wash) 0%, rgba(230,236,243,0.35) 35%, var(--paper) 55%, rgba(230,236,243,0.6) 85%, var(--wash) 100%);
  }
  .brand {
    position: absolute;
    left: 84px;
    top: 236px;
    display: flex;
    align-items: center;
    gap: 14px;
  }
  .brand__dot {
    width: 26px;
    height: 26px;
    border-radius: 50%;
    background: var(--accent);
  }
  .brand__name {
    font-weight: 700;
    font-size: 40px;
    letter-spacing: 1px;
    color: var(--ink);
    white-space: nowrap;
  }
  .contact {
    position: absolute;
    right: 86px;
    top: 0;
    text-align: right;
    white-space: nowrap;
  }
  .contact__name {
    position: absolute;
    right: 0;
    top: 72px;
    margin: 0;
    font-size: 65px;
    font-weight: 700;
    letter-spacing: -0.5px;
    line-height: 1;
  }
  .contact__line {
    position: absolute;
    right: 0;
    margin: 0;
    font-size: 48px;
    font-weight: 400;
    line-height: 1;
  }
  .contact__phone { top: 214px; }
  .contact__email { top: 270px; }
  .contact__street { top: 386px; }
  .contact__city { top: 442px; }
  .services {
    position: absolute;
    left: 86px;
    right: 84px;
    top: 592px;
    margin: 0;
    padding: 0;
    list-style: none;
    display: flex;
    justify-content: space-between;
    align-items: center;
    font-size: 24px;
    font-weight: 700;
    letter-spacing: 3.6px;
    word-spacing: 6px;
  }
  .services__sep {
    width: 12px;
    height: 12px;
    border-radius: 50%;
    background: var(--accent);
  }
</style>
</head>
<body>
  <main class="card">
    <div class="card__backdrop" role="img" aria-label="Soft pale blue background wash"></div>

    <div class="brand">
      <span class="brand__dot"></span>
      <span class="brand__name">Qovo International</span>
    </div>

    <div class="contact">
      <h1 class="contact__name">Dennis Marlow</h1>
      <p class="contact__line contact__phone">+61 427581962</p>
      <p class="contact__line contact__email">dennis@qovo.com.au</p>
      <p class="contact__line contact__street">P.O. Box 872</p>
      <p class="contact__line contact__city">Kelvindale QLD 4309</p>
    </div>

    <ul class="services">
      <li>Film Services</li>
      <li class="services__sep" aria-hidden="true"></li>
      <li>Pilot Escorts</li>
      <li class="services__sep" aria-hidden="true"></li>
      <li>Tour Management</li>
      <li class="services__sep" aria-hidden="true"></li>
      <li>Driver</li>
    </ul>
  </main>
</body>
</html>
```